Womans Supplement Designs

Launching a Supplement company and need to get some initial designs created, I've attached our logo and the bottle type that I want the samples done one.

This project is for our Whey Protein we are starting with Vanilla, chocolate and strawberry banana

(ALL DESIGN VARIATIONS MUST BE A WHITE BOTTLE NOT BLACK)

(FOR DESIGN SAMPLES PLEASE USE THE SUPPLEMENT BOTTLE STYLE I PROVIDED)

Whoever is selected the winner I will have more work for you to complete the disigns for the rest of the products in the line, Just want to get this shake completed first

Target Market(s)

Women

Requirements
Must have
• Must have our current logo involved

the name of this product will be "KIVA LUM"

Must have this slogan,

ALL-IN-ONE PREMIUM PROTEIN NUTRITIONAL SHAKE FOR BLACK WOMEN

This is our meal replacement

the design should try to keep the same look and feel of the existing provided supplement images

we are starting with chocolate, vanilla and strawberry banana

this is for women and should look colorful and appeal to them
Should not have
• Do not use an image of a person or lady, don't want it branded to a person

```html
<!DOCTYPE html>
<html lang="en">
<head>
<meta charset="utf-8">
<title>Kiva Lum Whey Protein – Vanilla Label</title>
<link rel="stylesheet" href="https://fonts.googleapis.com/css2?family=Titan+One&family=Oswald:wght@600;700&family=Montserrat:wght@500&display=swap">
<style>
  :root {
    --page-bg: #e9e8ea;
    --label-pink: #f2c3e8;
    --label-pink-light: #fbe6f6;
    --plum-dark: #3b0f35;
    --plum: #7a1f5e;
    --magenta: #b43a7c;
    --magenta-bright: #d24c92;
    --silver-light: #ffffff;
    --silver-mid: #c9c9cf;
    --silver-dark: #8e8e96;
    --ink: #111111;
    --white: #ffffff;
    --vanilla-flower: #f4ecb0;
    --vanilla-pod: #4a2a1a;
  }
  * { margin: 0; padding: 0; box-sizing: border-box; }
  html, body {
    width: 1200px;
    height: 675px;
    overflow: hidden;
    background: var(--page-bg);
  }
  .canvas {
    width: 1200px;
    height: 675px;
    display: flex;
    align-items: center;
    justify-content: center;
  }
  .label { display: block; width: 720px; height: 563px; box-shadow: 0 8px 24px rgba(60, 20, 50, 0.15); }
  .brand-name { font-family: "Montserrat", sans-serif; font-weight: 500; fill: var(--white); }
  .product-name { font-family: "Titan One", sans-serif; }
  .product-type { font-family: "Titan One", sans-serif; fill: var(--white); stroke: var(--ink); stroke-width: 3; paint-order: stroke; }
  .slogan { font-family: "Oswald", sans-serif; font-weight: 700; fill: var(--ink); }
  .macro-label { font-family: "Titan One", sans-serif; fill: var(--white); }
  .macro-value { font-family: "Titan One", sans-serif; fill: var(--white); }
  .flavour { font-family: "Oswald", sans-serif; font-weight: 700; fill: var(--white); letter-spacing: 1px; }
  .net-weight { font-family: "Titan One", sans-serif; fill: var(--white); }
  .supplement-note { font-family: "Oswald", sans-serif; font-weight: 600; fill: var(--ink); }
</style>
</head>
<body>
<main class="canvas">
  <svg class="label" viewBox="0 0 610 477" xmlns="http://www.w3.org/2000/svg">
    <defs>
      <radialGradient id="label-bg" cx="50%" cy="50%" r="70%">
        <stop offset="0" stop-color="var(--label-pink-light)"/>
        <stop offset="1" stop-color="var(--label-pink)"/>
      </radialGradient>
      <linearGradient id="banner-fill" x1="0" y1="0" x2="1" y2="0">
        <stop offset="0" stop-color="var(--magenta)"/>
        <stop offset="0.5" stop-color="var(--plum)"/>
        <stop offset="1" stop-color="var(--plum-dark)"/>
      </linearGradient>
      <linearGradient id="swoosh-fill" x1="0" y1="0" x2="1" y2="0">
        <stop offset="0" stop-color="var(--magenta-bright)"/>
        <stop offset="0.55" stop-color="var(--magenta)"/>
        <stop offset="1" stop-color="var(--plum)"/>
      </linearGradient>
      <linearGradient id="silver-fill" x1="0" y1="0" x2="0" y2="1">
        <stop offset="0" stop-color="var(--silver-light)"/>
        <stop offset="0.5" stop-color="var(--silver-mid)"/>
        <stop offset="1" stop-color="var(--silver-dark)"/>
      </linearGradient>
      <radialGradient id="vanilla-fill" cx="50%" cy="40%" r="60%">
        <stop offset="0" stop-color="var(--vanilla-flower)"/>
        <stop offset="1" stop-color="var(--vanilla-pod)" stop-opacity="0.85"/>
      </radialGradient>
    </defs>

    <!-- label ground -->
    <rect class="label-ground" width="610" height="477" fill="url(#label-bg)"/>

    <!-- brand banner -->
    <g class="brand-banner">
      <path d="M65 0 H512 C506 46 478 82 420 92 C300 106 160 110 65 120 Z" fill="url(#banner-fill)"/>
      <circle cx="172" cy="50" r="18" fill="var(--white)"/>
      <text class="brand-name" x="230" y="45" font-size="21" letter-spacing="2">NOVA GRACE</text>
      <text class="brand-name" x="231" y="68" font-size="11" letter-spacing="6">LIFESTYLE</text>
      <text class="brand-name" x="231" y="86" font-size="7" letter-spacing="1.5">NUTRITION</text>
    </g>

    <!-- product title -->
    <g class="product-title">
      <text class="product-name" x="296" y="224" font-size="86" text-anchor="middle"
            fill="url(#silver-fill)" stroke="var(--magenta-bright)" stroke-width="2.5"
            paint-order="stroke" transform="skewX(-8) translate(32 0)">KIVA LUM</text>
      <text class="product-type" x="292" y="271" font-size="36" text-anchor="middle">Whey Protein</text>
    </g>

    <!-- slogan -->
    <g class="slogan-block" transform="rotate(-4 292 320)">
      <text class="slogan" x="292" y="312" font-size="21" text-anchor="middle" textLength="272" lengthAdjust="spacingAndGlyphs">ALL-IN-ONE PREMIUM PROTEIN</text>
      <text class="slogan" x="292" y="340" font-size="21" text-anchor="middle" textLength="346" lengthAdjust="spacingAndGlyphs">NUTRITIONAL SHAKE FOR BLACK WOMEN</text>
    </g>

    <!-- flavour swoosh -->
    <g class="flavour-band">
      <path d="M70 477 C74 430 130 400 250 385 L596 310 L610 477 Z" fill="url(#swoosh-fill)"/>
      <path d="M70 477 C80 440 140 418 250 405 L600 360 L600 372 L252 416 C150 430 96 450 88 477 Z" fill="var(--magenta-bright)" opacity="0.45"/>
    </g>

    <!-- macro boxes -->
    <g class="macro-boxes">
      <rect x="158" y="381" width="62" height="50" fill="var(--magenta)" stroke="var(--white)" stroke-width="1.5"/>
      <text class="macro-label" x="189" y="396" font-size="10" text-anchor="middle">Protein</text>
      <text class="macro-value" x="189" y="424" font-size="22" text-anchor="middle">60%</text>
      <rect x="224" y="381" width="64" height="50" fill="var(--magenta)" stroke="var(--white)" stroke-width="1.5"/>
      <text class="macro-label" x="256" y="396" font-size="10" text-anchor="middle">Carb</text>
      <text class="macro-value" x="256" y="424" font-size="22" text-anchor="middle">40%</text>
    </g>

    <!-- flavour name and artwork area -->
    <text class="flavour" x="328" y="402" font-size="34">VANILLA</text>
    <g role="img" aria-label="Vanilla flower with vanilla bean pods">
      <ellipse cx="535" cy="385" rx="50" ry="55" fill="url(#vanilla-fill)" opacity="0.9"/>
    </g>

    <!-- net weight -->
    <text class="net-weight" x="378" y="470" font-size="22">2 lb (948g)</text>

    <!-- dietary supplement strip -->
    <g class="supplement-strip">
      <path d="M70 444 H250 C290 444 305 460 320 477 H70 Z" fill="var(--white)"/>
      <path d="M70 444 H250 C290 444 305 460 320 477" fill="none" stroke="var(--magenta-bright)" stroke-width="2"/>
      <text class="supplement-note" x="94" y="470" font-size="15" letter-spacing="0.5">DIETARY SUPPLEMENT</text>
    </g>
  </svg>
</main>
</body>
</html>
```